Pelmora Swifts Stridefair - 2 posters

We need two community event posters for an annual marathon with continuity in design showcasing the clubs logo colours and community spirit. Poster one is for the Juniors division which needs to look like a fun day encouraging families to come down and register and compete. It will be distributed to all the schools and social media. Poster two is for the main event again attracting registration with prizes. Encouraging all levels of runners from professionals to amateurs family friendly. It is in a unique location along the city's foreshore with amazing views.

Target Market(s)

Marathon runners, juniors, community and families

Requirements
Must have
• photos, logos details
Nice to have
• We are looking for a motivating high energy poster to entice registration and feel like fun event for the whole comminty

```html
<!DOCTYPE html>
<html lang="en">
<head>
<meta charset="utf-8">
<title>Swifts Junior Stridefair 2018</title>
<link href="https://fonts.googleapis.com/css2?family=Oswald:wght@500;600;700&family=Lato:wght@400;700;900&display=swap" rel="stylesheet">
<style>
  :root {
    --red: #e3262f;
    --teal: #1ba7c0;
    --orange: #f08a24;
    --navy: #1d3768;
    --green: #0e8a6a;
    --ink: #1c1c1c;
    --white: #ffffff;
    --band: rgba(240, 242, 245, 0.93);
  }
  * { margin: 0; padding: 0; box-sizing: border-box; }
  html, body { width: 867px; height: 1200px; overflow: hidden; background: #e9e9e9; }
  .poster { position: relative; width: 867px; height: 1200px; overflow: hidden; font-family: "Lato", sans-serif; }
  .hero-photo {
    position: absolute; inset: 0;
    background: linear-gradient(180deg, #e7e9ec 0%, #d7dce0 30%, #aac3c6 38%, #8fb4b6 50%, #cdbfa8 62%, #b8a88e 78%, #8e8a80 100%);
  }
  .club-mark { position: absolute; left: 44px; top: 36px; width: 290px; text-align: center; color: var(--navy); font-family: "Oswald", sans-serif; font-weight: 600; }
  .club-mark .dot { width: 120px; height: 120px; border-radius: 50%; background: var(--teal); margin: 0 auto 8px; }
  .club-mark .line-sm { font-size: 28px; line-height: 1.1; }
  .club-mark .line-lg { font-size: 66px; line-height: 1; text-transform: uppercase; }
  .club-mark .line-md { font-size: 27px; line-height: 1.15; letter-spacing: 3px; text-transform: uppercase; }
  .event-title { position: absolute; right: 44px; top: 22px; text-align: right; font-family: "Oswald", sans-serif; font-weight: 700; }
  .event-year { color: var(--red); font-size: 160px; line-height: 1; }
  .event-division { color: var(--teal); font-size: 40px; line-height: 1.1; margin-top: 10px; }
  .event-name { color: var(--orange); font-size: 80px; line-height: 1; margin-top: 6px; }
  .event-when { position: absolute; right: 44px; top: 325px; text-align: right; font-weight: 700; font-size: 28px; line-height: 1.5; color: var(--ink); }
  .race-info { position: absolute; left: -42px; top: 546px; width: 422px; height: 422px; border-radius: 50%; background: rgba(14, 138, 106, 0.9); }
  .race-copy { position: absolute; left: 41px; top: 610px; color: var(--white); font-size: 21px; line-height: 1.45; }
  .race-copy .start { font-weight: 700; font-size: 24px; margin-bottom: 12px; }
  .race-copy ul { list-style: none; margin-bottom: 14px; }
  .race-copy li::before { content: "• "; }
  .race-copy p { font-size: 23px; line-height: 1.2; margin-bottom: 10px; }
  .sponsor-band { position: absolute; left: 0; top: 951px; width: 867px; height: 122px; background: var(--band); }
  .sponsor-tab { position: absolute; left: 363px; top: 0; width: 138px; height: 22px; background: var(--navy); color: var(--white); font-size: 15px; text-align: center; line-height: 22px; }
  .sponsor-row { position: absolute; left: 36px; right: 36px; top: 38px; height: 62px; display: flex; justify-content: space-between; align-items: center; }
  .sponsor { display: flex; align-items: center; gap: 6px; color: var(--navy); font-weight: 700; font-size: 15px; }
  .sponsor .mark { width: 16px; height: 16px; border-radius: 50%; background: var(--navy); }
  .footer-band { position: absolute; left: 0; top: 1073px; width: 867px; height: 127px; background: var(--navy); color: var(--white); }
  .thanks { position: absolute; left: 44px; right: 44px; top: 14px; font-size: 11px; line-height: 1.4; }
  .tags { position: absolute; left: 44px; right: 44px; top: 82px; display: flex; justify-content: space-between; font-size: 22px; }
</style>
</head>
<body>
<div class="poster">
  <div class="hero-photo" role="img" aria-label="Photo of junior runners racing along a seaside path beside a rock wall and calm sea under a cloudy sky"></div>

  <div class="club-mark">
    <div class="dot"></div>
    <div class="line-sm">Pelmora Swifts</div>
    <div class="line-lg">Stridefair</div>
    <div class="line-md">&amp; Marathon</div>
  </div>

  <div class="event-title">
    <div class="event-year">2018</div>
    <div class="event-division">SWIFTS JUNIOR</div>
    <div class="event-name">STRIDEFAIR</div>
  </div>

  <div class="event-when">
    <div>Saturday June 30, 2018</div>
    <div>Foreshore - Pelmora Yacht Club</div>
  </div>

  <div class="race-info"></div>
  <div class="race-copy">
    <div class="start">Races start 4.00pm</div>
    <ul>
      <li>1 mile (1.6km) 3-6 years old</li>
      <li>2 miles (3.2km) 7-11 years old</li>
      <li>3 miles (4.8km) 12-16 years old</li>
    </ul>
    <p>Great prizes &amp; fun<br>for the whole family</p>
    <p>Don’t miss out register at<br>pelmorastridefair.com</p>
  </div>

  <div class="sponsor-band">
    <div class="sponsor-tab">SPONSOR</div>
    <div class="sponsor-row">
      <div class="sponsor"><span class="mark"></span>Pelmora Swifts</div>
      <div class="sponsor">Tallow Health</div>
      <div class="sponsor">Greater Pelmora</div>
      <div class="sponsor">Corvine Mobile</div>
      <div class="sponsor">Zenlo Events</div>
      <div class="sponsor">Marrick Supermarkets</div>
    </div>
  </div>

  <div class="footer-band">
    <p class="thanks">Pelmora Swifts Club proudly presents this event to the Community with thanks to generous Sponsors, Partners and Volunteers including: Brenley Electrical | Stride Shed | Coastline Sparks | The Harbourline Apartments | Toastie Hut | Orin Vale Jewellers | Core Nine | Pelmora Motors | Tom Kessly MLA | Cuppa Hall | Mira Dalton Wellness | Topfuel Co | Pharmacy Eleven | Sport Central | Pelmora Foot Clinic | Harlow &amp; Finch | Coast Rescue | Linden Ross Homes | Brightway Print</p>
    <div class="tags">
      <span>#swiftsstridefair</span><span>|</span><span>#wearechampions</span><span>|</span><span>#fitnessforlife</span>
    </div>
  </div>
</div>
</body>
</html>
```